Coralbay Realty Letterhead

Coralbay Realty Guan
418 Maru Tasi Loop, Ste B207
Tumon, GU. 96928

Industry/Entity Type

Real Estate

Font styles to use
Serif

Colors

Designer to choose colors to be used in the design.

```html
<!DOCTYPE html>
<html lang="en">
<head>
<meta charset="utf-8">
<title>Coralbay Realty Letterhead</title>
<link href="https://fonts.googleapis.com/css2?family=Open+Sans:wght@300;400&family=Tinos:wght@400;700&family=Great+Vibes&display=swap" rel="stylesheet">
<style>
  :root {
    --backdrop: #e3e3e3;
    --paper: #f2f2f2;
    --ink: #3a3a3a;
    --brand-blue: #1a8ac7;
    --brand-light: #4fb3df;
    --white: #ffffff;
  }
  html, body {
    margin: 0;
    padding: 0;
    width: 1200px;
    height: 1200px;
    overflow: hidden;
    background: var(--backdrop);
  }
  .letterhead {
    position: absolute;
    left: 200px;
    top: 35px;
    width: 800px;
    height: 1130px;
    background: var(--paper);
    box-shadow: 0 2px 10px rgba(0,0,0,0.12);
    font-family: "Open Sans", sans-serif;
    color: var(--ink);
  }
  .brand-name {
    position: absolute;
    top: 100px;
    left: 0;
    width: 100%;
    text-align: center;
    font-family: "Open Sans", sans-serif;
    font-weight: 300;
    font-size: 34px;
    letter-spacing: 3px;
    color: var(--brand-light);
    margin: 0;
  }
  .letter-body {
    position: absolute;
    left: 108px;
    top: 265px;
    width: 584px;
    font-weight: 300;
    font-size: 13.4px;
    line-height: 18.8px;
  }
  .salutation { margin: 0 0 18px; }
  .letter-body p.paragraph {
    margin: 0 0 18.5px;
    text-align: justify;
  }
  .closing {
    position: absolute;
    left: 108px;
    top: 773px;
    font-weight: 300;
    font-size: 13.4px;
    margin: 0;
  }
  .signature {
    position: absolute;
    left: 114px;
    top: 796px;
    font-family: "Great Vibes", cursive;
    font-size: 28px;
    color: #222;
    margin: 0;
  }
  .footer-band {
    position: absolute;
    left: 0;
    top: 1086px;
    width: 100%;
    height: 31px;
    background: var(--brand-blue);
    color: var(--white);
    font-family: "Tinos", serif;
    font-size: 13.5px;
    line-height: 31px;
    text-align: center;
  }
  .footer-band strong { font-weight: 700; }
</style>
</head>
<body>
  <main class="letterhead">
    <h1 class="brand-name">CORALBAY REALTY</h1>

    <section class="letter-body">
      <p class="salutation">Dear Daniel Arbury,</p>
      <p class="paragraph">Lorem ipsum dolor sit amet, consectetuer adipiscing elit, sed diam nonummy nibh euismod tincidunt ut laoreet dolore magna aliquam erat volutpat. Ut wisi enim ad minim veniam, quis nostrud exerci tation ullamcorper suscipit lobortis nisl ut aliquip ex ea commodo consequat. Duis dolore te feugait nulla facilisi. Nam liber tempor cum soluta nobis eleifend option congue nihil imperdiet doming id quod mazim placerat facer possim assum. Lorem ipsum dolor sit amet, consectetuer adipiscing elit, sed diam nonummy nibh euismod tincidunt ut laoreet dolore magna aliquam erat volutpat. Ut wisi enim ad minim veniam, quis nostrud exerci tation ullamcorper suscipit lobortis nisl ut aliquip ex ea commodo consequat.</p>
      <p class="paragraph">Consectetuer adipiscing elit, sed diam nonummy nibh euismod tincidunt ut laoreet dolore magna aliquam erat volutpat. Ut wisi enim ad minim veniam, quis nostrud exerci tation ullamcorper suscipit lobortis nisl ut aliquip ex ea commodo consequat. Consectetuer adipiscing elit, sed diam nonummy nibh euismod tincidunt ut laoreet dolore magna aliquam erat volutpat. Ut wisi enim ad minim veniam, quis nostrud exerci tation ullamcorper suscipit lobortis nisl ut aliquip ex ea commodo consequat.</p>
      <p class="paragraph">Consectetuer adipiscing elit, sed diam nonummy nibh euismod tincidunt ut laoreet dolore magna aliquam erat volutpat. Ut wisi enim ad minim veniam, quis nostrud exerci tation ullamcorper suscipit lobortis nisl ut aliquip ex ea commodo consequat. Consectetuer adipiscing elit, sed diam nonummy nibh euismod tincidunt ut laoreet dolore magna aliquam erat volutpat. Ut wisi enim ad minim veniam, quis nostrud exerci tation ullamcorper suscipit lobortis nisl ut aliquip ex ea commodo consequat.</p>
    </section>

    <p class="closing">Sincerely Yours</p>
    <p class="signature">Marcus Halvorsen</p>

    <footer class="footer-band">
      <strong>Coralbay Realty Guan,</strong> 418 Maru Tasi Loop, Ste B207, Tumon, GU. 96928
    </footer>
  </main>
</body>
</html>
```